Lumen Gathering 2019 Enemies of the End-Times Church Flyer

We want a church conference flyer designed. We are looking for a professional, yet catchy design that uses our brand colors and logo creatively while communicating key information of the event effectively. <br/>The flyer must include all of the following:<br/>Title: Lumen Gathering 2019<br/>Topic: The Enemies of The End-Times Church <br/>Subtitles: <br/> -How the antichrist raises an army by social behavior engineering. <br/>-How the architects of modern social constructs escaped the church's radar. <br/>-The Holy Spirit's end-times agenda:<br/> The Knock-Out Punch!<br/>Speaker: Prophet Marcus Obuya <br/>Dates/time: December 27, 28 & 29 at 6pm<br/>Location: Thistle Community Center <br/> 412 Farrow Lane <br/> Portland, ME 04219<br/>Contact info: phone: 207-583-1924 <br/>email: contact@vellorbrook.org <br/> www.toskin.org<br/>*The flyer must also include a picture of the speaker and our Toskin logo <br/>Thanks, we look forward to seeing what you come up with!

Colors

Designer to choose colors to be used in the design.

Requirements
Must have
• The flyer must include all of the following:
• Title: Lumen Gathering 2019
• Topic: The Enemies of The End-Times Church
• Subtitles:
• -How the antichrist raises an army by social behavior engineering.
• -How the architects of modern social constructs escaped the church's radar.
• -The Holy Spirit's end-times agenda:
• The Knock-Out Punch!
• Speaker: Prophet Marcus Obuya
• Dates/time: December 27, 28 & 29 at 6pm
• Location: Thistle Community Center
• 412 Farrow Lane
• Portland, ME 04219
• Contact info: phone: 207-583-1924
• email: contact@vellorbrook.org
• www.toskin.org
• *The flyer must also include a picture of the speaker and our Toskin logo
Should not have
• Pictures of crosses or church buildings

```html
<!DOCTYPE html>
<html lang="en">
<head>
<meta charset="utf-8">
<title>Lumen Gathering 2019 — The Enemies of the End-Times Church</title>
<link rel="stylesheet" href="https://fonts.googleapis.com/css2?family=Alfa+Slab+One&family=Open+Sans:wght@400;600&display=swap">
<style>
  :root {
    --paper: #ebebeb;
    --teal: #23888f;
    --ink: #1e1e1e;
    --black: #141414;
    --white: #ffffff;
    --brand-orange: #e8831f;
    --photo-light: #8d8a86;
    --photo-dark: #2b2a2c;
  }
  * { margin: 0; padding: 0; box-sizing: border-box; }
  html, body { width: 927px; height: 1200px; overflow: hidden; background: var(--paper); }
  .flyer {
    position: relative; width: 927px; height: 1200px; overflow: hidden;
    background: var(--paper);
    font-family: "Open Sans", Arial, sans-serif; color: var(--ink);
  }
  .decor { position: absolute; left: 0; top: 0; }

  .brand {
    position: absolute; left: 85px; top: 73px; width: 146px; height: 94px;
    background: var(--white);
    display: flex; align-items: center; justify-content: center; gap: 8px;
  }
  .brand-dot { width: 14px; height: 14px; border-radius: 50%; background: var(--brand-orange); }
  .brand-name { font-weight: 600; font-size: 26px; color: var(--teal); letter-spacing: 0.5px; }

  .topic {
    position: absolute; left: 85px; top: 300px;
    color: var(--teal); font-size: 36px; line-height: 45px; font-weight: 400;
    text-transform: none;
  }

  .speaker-label {
    position: absolute; left: 528px; top: 462px; width: 250px;
    color: var(--white); text-align: center;
  }
  .speaker-name {
    font-size: 15px; font-weight: 600; letter-spacing: 0.6px;
    padding-bottom: 6px; border-bottom: 1px solid rgba(255,255,255,0.75);
  }
  .speaker-role { font-size: 13px; margin-top: 4px; }

  .event-title {
    position: absolute; left: 91px; top: 569px; width: 290px; height: 290px;
    display: flex; flex-direction: column; align-items: center; justify-content: center;
    color: var(--white); text-align: center;
  }
  .event-name { font-family: "Alfa Slab One", Georgia, serif; font-size: 52px; line-height: 1; letter-spacing: 1px; }
  .event-sub { font-size: 14px; letter-spacing: 1px; margin-top: 26px; }

  .sessions {
    position: absolute; left: 516px; top: 690px; width: 380px;
    list-style: none; font-size: 16.5px; line-height: 27px; color: var(--ink);
  }
  .sessions li + li { margin-top: 25px; }

  .dates {
    position: absolute; left: 85px; top: 990px;
    color: var(--teal); font-size: 36px; letter-spacing: 0.3px;
  }

  .info { position: absolute; font-size: 13px; line-height: 20px; color: var(--ink); }
  .venue { left: 85px; top: 1054px; }
  .web { left: 391px; top: 1060px; }
  .phone { left: 85px; top: 1105px; }
  .email { left: 391px; top: 1105px; }
</style>
</head>
<body>
<main class="flyer">
  <svg class="decor" width="927" height="1200" viewBox="0 0 927 1200" aria-hidden="true">
    <defs>
      <linearGradient id="photo-tone" x1="0" y1="0" x2="1" y2="1">
        <stop offset="0" stop-color="var(--photo-light)"/>
        <stop offset="0.55" stop-color="#5b5553"/>
        <stop offset="1" stop-color="var(--photo-dark)"/>
      </linearGradient>
    </defs>
    <circle cx="578" cy="269" r="300" fill="none" stroke="var(--black)" stroke-width="4"
            stroke-linecap="round" stroke-dasharray="0.1 11" />
    <line x1="335" y1="600" x2="428" y2="527" stroke="var(--black)" stroke-width="4"/>
    <line x1="465" y1="618" x2="465" y2="892" stroke="var(--black)" stroke-width="1.5"/>
    <g fill="var(--black)">
      <circle cx="520" cy="908" r="3.5"/><circle cx="543" cy="908" r="3.5"/><circle cx="566" cy="908" r="3.5"/><circle cx="589" cy="908" r="3.5"/>
      <circle cx="520" cy="932" r="3.5"/><circle cx="543" cy="932" r="3.5"/><circle cx="566" cy="932" r="3.5"/><circle cx="589" cy="932" r="3.5"/>
      <circle cx="520" cy="956" r="3.5"/><circle cx="543" cy="956" r="3.5"/><circle cx="566" cy="956" r="3.5"/><circle cx="589" cy="956" r="3.5"/>
    </g>
    <circle cx="236" cy="714" r="145" fill="var(--black)"/>
  </svg>

  <svg class="decor" width="927" height="1200" viewBox="0 0 927 1200" role="img"
       aria-label="Portrait photo of speaker Prophet Marcus Obuya in front of bookshelves">
    <circle cx="578" cy="269" r="276" fill="url(#photo-tone)"/>
  </svg>

  <div class="brand"><span class="brand-dot"></span><span class="brand-name">Toskin</span></div>

  <h1 class="topic">THE ENEMIES<br>of the<br>END - TIMES<br>CHURCH</h1>

  <div class="speaker-label">
    <p class="speaker-name">PROPHET MARCUS OBUYA</p>
    <p class="speaker-role">speaker</p>
  </div>

  <div class="event-title">
    <p class="event-name">LUMEN</p>
    <p class="event-sub">GATHERING 2019</p>
  </div>

  <ul class="sessions">
    <li>How the antichrists raises an army<br>by social behavior engineering</li>
    <li>How the architects of modern social<br>constructs escaped the church's radar</li>
    <li>The Holy Spirit's end - times agenda:<br>The Knock - Out Punch!</li>
  </ul>

  <p class="dates">DECEMBER 27, 28 &amp; 29, 2019 at 6 PM</p>

  <p class="info venue">Thistle Community Center<br>412 Farrow Lane Portland, ME 04219</p>
  <p class="info web">Visit us at www.toskin.org</p>
  <p class="info phone">Contact info: 207-583-1924</p>
  <p class="info email">Email: contact@vellorbrook.org</p>
</main>
</body>
</html>
```